Fresh and Trendy Daily Deals Aggregator in 17 countries in Europe needs your web design inspiration to inspire the buying masses. We are a young, fresh, crazy and dynamic team and we plan to take the daily deals space by storm very soon. fizzbark will bring a completely fresh approach to giving people amazing discount offers from daily deal sites, such as Tallymob, HappyTowner and others for things like spa treatments, fitness, clubs, restaurants, online shopping, offers, health, beauty... Be a part of a happening!

We are looking for a web design with no coding for an ajax-based website (we need PSD, no HTML/CSS). We are looking for something that will look fresh and not too techy. Needs to be very readable - so a nice contrast between font and background and a readable font. We really like the simplicity of chatrove, peepline: light, fun, simple to read, modern, minimalist, easy to navigate.

We also like the following landers:

Chatrove (Simple colors and easy to navigate)
HappyTowner.com (nice image as the background)
Tallymob.com (Simple colors and easy to navigate)
http://plumvoyage-example.com/ (Nice site ambience and nice skin)
http://www.vexoffre-example.fr/city,paris,tous-les-bons-plans.html (Map View with little deal icons showing the location and type of deal)
http://www.brightpinatlas-example.com (Map View with little deal icons showing the location and type of deal)

We want something hip and trendy, fun and fresh but DIFFERENT from all the rest out there. We'd also want to keep the number of user clicks to the bare minimum possible.

Reason: Hello! Since most of the designs are still going through revisions we've decided to extend the deadline to give everybody the best chance of completing their designs. Thanks so far for all the great designs! Otto FIZZBARK

Target Market(s)

Our target audience is: Trendy, active people who like to go out several times per week, they have money, educated, between 18 and 40 years old and fa

Industry/Entity Type

Fitness

Requirements
Must have
• Design Specs:

- MUST HAVE ALL THE FILTERS SEEN ON OUR TEST SITE (see below for URL and login details)
- MUST BE ABLE TO SEE LOTS OF DEALS PER PAGE BECAUSE WE ARE A DAILY DEALS AGGREGATOR AND HAVE HUNDREDS OF DEALS.
- The width needs to be a size that will work with every size computer screen
* Need to use cross-platform compatible font (Google webfonts ok)
- The graphic elements used for the design must be copyright free

You can find our current test site here:

http://zrv.mivo-tokens-example.com

Username: designers@mivo-tokens-example.com
Password: Kestrel42

This is a very basic version, all functionnalities are not working yet, and we are looking to you to make it all make graphical sense to the user so that it's ultra easy to understand and to navigate through.

Our Logo has been uploaded as PSD files with all the color variations. Please base the color scheme of the site on the colors of the logo but feel free to use lighter or darker shades of the same colors as well as black, grays or white, if necessary.

The CMYK for each color is:

Green: C40 & Y100
Pink: M86

Be creative and refer often back to the web 2.0 landers above.

IMPORTANT NOTES REGARDING OUR CURRENT TEST SITE:
Fell free to group elements differently or to hide them under pop- ups, to resize them or to change them in any way that works with your design. The only constraint is that all of the functions must be easily accessible to the user.

We would like to have little icons signifying each category. On our test site, all the categories might not be visible but the categories are: Dining, Health & Beauty, Style, Nightlife, Education & Training, Shopping, Travel, Special Interest, Events, Services, Fitness, Other.

The second tab of the site is a map view and we'd like the little category icons to be used as the points that show where the deals are located and the kind of deals that are located there. (For regerence see http://www.brightpinatlas-example.com/#DynamicContentContainer AND http://www.vexoffre-example.fr/city,paris,tous-les-bons-plans.html)

Fizzbark is currently aggregating deals from 17 European countries and we need to make it easy for the user to navigate from one country to another.

On our test site you will see country flags at the top of the page. If we could have the name of each country next to its flag without sacrificing too much space it would be better. But, if you find an even better way to make this work feel free to do so. Also, at the bottom of the page we have all the cities in which we have deals, and the list gets very long. If you could design another way to let the user see the countries/cities/deals via the bottom page links it would save space.

Also, when you log in to our test site you will see a pop-up. The text of the pop-up should only be: "Let FizzBark save you precious time and find your perfect deals so you can sit back, relax and enjoy. Tell us what you like and how you like it and we'll deliver personalized deals right to your inbox. Or use our convenient selectors to see all the deals that are just right for you."

Finally, the banner at the top of the page that reads: "SELL ONLINE" should say: "Sell your own deals through FizzBark!

Accepted file formats: During the design phase adobe PSD and JPEG are OK (if you need to upload files), but for the handover we'll need PSD only with all the original layers.

```html
<!DOCTYPE html>
<html lang="en">
<head>
<meta charset="utf-8">
<title>fizzbark – find your perfect deal</title>
<link rel="stylesheet" href="https://fonts.googleapis.com/css2?family=Arimo:wght@400;700&family=Oswald:wght@500;700&display=swap">
<style>
:root{
  --pink:#e5177b;
  --green:#7ab51d;
  --panel:rgba(38,30,24,.9);
  --bar:#2e2823;
  --sheet:rgba(255,255,255,.62);
  --ink:#5b5b5b;
  --ink-soft:#6d6d6d;
  --share:#2a8fd8;
  --backdrop-top:#4a9fe0;
  --backdrop-bottom:#e2b550;
}
*{box-sizing:border-box;margin:0;padding:0}
html,body{width:1200px;height:881px;overflow:hidden}
body{position:relative;font-family:"Arimo",Arial,sans-serif;color:var(--ink)}
.backdrop{position:absolute;inset:0;background:linear-gradient(180deg,var(--backdrop-top) 0%,#a9d4ee 50%,var(--backdrop-bottom) 100%)}
.abs{position:absolute}

/* top bar */
.topbar{left:234px;top:20px;width:732px;height:28px;background:var(--bar);border-radius:4px}
.field{background:#fff;font-size:10px;color:#444;padding:2px 5px;height:15px;line-height:11px}
.btn-green{background:var(--green);color:#fff;font-size:9px;text-align:center;line-height:15px;height:15px}
.drop-arrow{position:absolute;right:0;top:0;width:14px;height:100%;background:var(--green)}
.drop-arrow::after{content:"";position:absolute;left:3px;top:4px;border-left:4px solid transparent;border-right:4px solid transparent;border-top:6px solid #fff}
.search-btn{background:var(--green)}
.search-btn svg{display:block}

/* language list */
.lang-list{left:680px;top:42px;width:102px;height:134px;background:#fff;box-shadow:0 2px 4px rgba(0,0,0,.3);z-index:5}
.lang-list li{list-style:none;height:17.8px;display:flex;align-items:center;padding-left:18px;font-size:7.5px;color:#222}
.flag{width:11px;height:8px;margin-right:7px}
.at{background:linear-gradient(#e1202f 33%,#fff 33% 66%,#e1202f 66%)}
.be{background:linear-gradient(90deg,#111 33%,#f6d516 33% 66%,#e1202f 66%)}
.bg{background:linear-gradient(#fff 33%,#1a9a54 33% 66%,#d62718 66%)}
.hr{background:linear-gradient(#e1202f 33%,#fff 33% 66%,#1c3f94 66%)}
.fr{background:linear-gradient(90deg,#1f4aa8 33%,#fff 33% 66%,#e1202f 66%)}
.de{background:linear-gradient(#111 33%,#e1202f 33% 66%,#f5c400 66%)}
.ie{background:linear-gradient(90deg,#1a9a54 33%,#fff 33% 66%,#f08a24 66%)}
.scroll{position:absolute;right:2px;top:2px;width:12px;height:130px;background:#eee}
.scroll::after{content:"";position:absolute;left:1px;top:14px;width:10px;height:16px;background:#fff;border:1px solid #bbb}

/* sidebar */
.sidebar{left:234px;top:63px;width:211px;height:740px;background:var(--panel);border-radius:6px 6px 0 0;color:#fff}
.brand{left:22px;top:16px;display:flex;align-items:center;gap:6px}
.brand-dot{width:40px;height:40px;border-radius:50%;background:var(--green)}
.brand-name{font-weight:700;font-size:32px;color:var(--pink);letter-spacing:-.5px}
.headline{left:0;width:211px;text-align:center;font-family:"Oswald",Impact,sans-serif;font-weight:700;color:#fff;line-height:1}
.h1a{top:96px;font-size:38px}
.h1b{top:140px;font-size:29px}
.pitch{left:20px;top:182px;width:172px;text-align:center;font-size:10.5px;line-height:13px}
.select{left:22px;width:166px;height:16px;background:#fff;color:#444;font-size:9px;line-height:16px;padding-left:5px}
.label-green{left:22px;color:var(--green);font-weight:700;font-size:13.5px}
.cats{left:22px;top:312px;list-style:none}
.cats li{height:19.6px;display:flex;align-items:center;font-size:8px}
.cat-ico{width:16px;height:16px;border-radius:2px;margin-right:5px}
.check{width:9px;height:9px;background:#fff;color:#333;font-size:8px;line-height:9px;text-align:center;margin-right:6px;flex:none}
.small{font-size:8px;left:22px}
.track{left:24px;width:138px;height:6px;background:#ddd;border-radius:3px}
.fill{position:absolute;top:0;height:6px;background:var(--green);border-radius:3px}
.knob{position:absolute;top:-3px;width:8px;height:12px;background:#fff;border:1px solid #999;border-radius:2px}
.radios{left:22px;font-size:7.5px;display:flex;gap:7px}
.radio{display:inline-block;width:5px;height:5px;border-radius:50%;background:#bbb;margin-right:2px;vertical-align:middle}
.radio.on{background:var(--green)}
.checks{left:22px;top:605px;font-size:8px;display:flex;align-items:center}
.keyword{left:22px;top:654px;width:151px;height:16px;background:#fff}

/* main */
.tabs{left:472px;top:63px;display:flex;gap:2px}
.tab{background:var(--pink);color:#fff;font-weight:700;font-size:11px;height:25px;line-height:25px;padding:0 9px}
.social{display:flex;gap:6px}
.sq{width:18px;height:18px;border-radius:2px}
.sq.s1{background:#3b64a8}.sq.s2{background:#4fb6e6}.sq.s3{background:#ee7f22}.sq.s4{background:#d62a2a}
.sheet{left:472px;top:88px;width:494px;height:793px;background:var(--sheet)}
.deal{position:absolute;left:472px;width:494px;height:157px}
.photo{position:absolute;left:18px;top:5px;width:170px;height:120px}
.share{position:absolute;left:19px;top:127px;display:flex;gap:4px;align-items:center}
.share .sq{width:12px;height:12px}
.share-pill{margin-left:10px;background:var(--share);color:#fff;font-size:7px;font-weight:700;border-radius:3px;padding:2px 5px}
.info{position:absolute;left:195px;top:4px;width:200px}
.title{font-size:12px;font-weight:700;color:var(--ink)}
.title em{font-style:normal;color:var(--green)}
.desc{font-size:8px;line-height:10px;color:var(--ink-soft);margin-top:2px;height:44px}
.meta{font-size:10px;font-weight:700;color:var(--ink);line-height:13px}
.price{font-family:"Oswald",Impact,sans-serif;font-weight:700;font-size:44px;line-height:48px;color:var(--ink);letter-spacing:-2px}
.stats{position:absolute;left:403px;top:3px;width:73px;font-size:8px;line-height:10.5px;color:var(--ink-soft)}
.stats div{display:flex;justify-content:space-between}
.cta{position:absolute;left:406px;width:70px;height:26px;border-radius:3px;color:#fff;font-family:"Oswald",Impact,sans-serif;font-weight:500;font-size:13px;text-align:center;line-height:26px}
.details{top:63px;background:var(--pink)}
.buy{top:97px;background:var(--green)}
.cut{position:absolute;left:18px;top:144px;width:440px;border-top:1px dashed #8a8a8a}
.scissors{position:absolute;left:461px;top:137px}
</style>
</head>
<body>
<div class="backdrop" role="img" aria-label="Full-page holiday beach photograph in blue sky and golden sand tones"></div>

<header class="abs topbar">
  <div class="abs field" style="left:8px;top:7px;width:118px">E-mail</div>
  <div class="abs btn-green" style="left:126px;top:7px;width:50px">subscribe</div>
  <div class="abs field" style="left:446px;top:7px;width:102px">select language<span class="drop-arrow"></span></div>
  <div class="abs field" style="left:556px;top:7px;width:155px">My searches</div>
  <div class="abs search-btn" style="left:711px;top:7px;width:13px;height:15px">
    <svg width="13" height="15" viewBox="0 0 13 15"><circle cx="6" cy="6.5" r="3" fill="none" stroke="#fff" stroke-width="1.4"/><line x1="8" y1="8.5" x2="10.5" y2="11" stroke="#fff" stroke-width="1.6"/></svg>
  </div>
</header>

<ul class="abs lang-list">
  <li><span class="flag at"></span>AUSTRIA</li>
  <li><span class="flag be"></span>BELGIUM</li>
  <li><span class="flag bg"></span>BULGARIA</li>
  <li><span class="flag hr"></span>CROATIA</li>
  <li><span class="flag fr"></span>FRANCE</li>
  <li><span class="flag de"></span>GERMANY</li>
  <li><span class="flag ie"></span>IRELAND</li>
  <span class="scroll"></span>
</ul>

<aside class="abs sidebar">
  <div class="abs brand"><span class="brand-dot"></span><span class="brand-name">fizzbark</span></div>
  <div class="abs headline h1a">FIND YOUR</div>
  <div class="abs headline h1b">PERFECT DEAL</div>
  <p class="abs pitch">"Select categories and sort by DISTANCE and PRICE and fizzbark will automatically find your perfect deals!"</p>
  <div class="abs select" style="top:244px">choose a country<span class="drop-arrow"></span></div>
  <div class="abs select" style="top:267px">select a city<span class="drop-arrow"></span></div>

  <div class="abs label-green" style="top:293px">select a category:</div>
  <ul class="abs cats">
    <li><span class="cat-ico" style="background:#8b6b3d"></span><span class="check">✓</span>dining (2)</li>
    <li><span class="cat-ico" style="background:#d8232a"></span><span class="check">✓</span>Health &amp; Wellness (3)</li>
    <li><span class="cat-ico" style="background:#e6177d"></span><span class="check">✓</span>beauty (5)</li>
    <li><span class="cat-ico" style="background:#f7941d"></span><span class="check">✓</span>style (15)</li>
    <li><span class="cat-ico" style="background:#1e9ad6"></span><span class="check">✓</span>events (5)</li>
    <li><span class="cat-ico" style="background:#3aa24a"></span><span class="check">✓</span>education &amp; training (10)</li>
    <li><span class="cat-ico" style="background:#c81e2a"></span><span class="check">✓</span>travel (5)</li>
    <li><span class="cat-ico" style="background:#f05a28"></span><span class="check">✓</span>shoping (3)</li>
    <li><span class="cat-ico" style="background:#7a3f98"></span><span class="check">✓</span>services (7)</li>
  </ul>

  <div class="abs small" style="top:495px">location distance</div>
  <div class="abs small" style="top:508px;font-size:7px;display:flex;align-items:center">include national:&nbsp;<span class="check">✓</span></div>
  <div class="abs track" style="top:522px"><span class="fill" style="left:0;width:26px"></span><span class="knob" style="left:22px"></span></div>

  <div class="abs small" style="top:537px">price range</div>
  <div class="abs track" style="top:552px"><span class="fill" style="left:14px;width:112px"></span><span class="knob" style="left:10px"></span><span class="knob" style="left:122px"></span></div>

  <div class="abs small" style="top:566px">deals per page</div>
  <div class="abs radios" style="top:581px"><span><i class="radio on"></i>10</span><span><i class="radio"></i>20</span><span><i class="radio"></i>30</span></div>
  <div class="abs radios" style="top:593px"><span><i class="radio"></i>50</span><span><i class="radio"></i>70</span><span><i class="radio"></i>100</span></div>
  <div class="abs checks"><span class="check">✓</span>discount&nbsp;&nbsp;<span class="check">✓</span>popularity&nbsp;&nbsp;<span class="check">✓</span>end date</div>

  <div class="abs label-green" style="top:623px">fine-tune by keyword:</div>
  <div class="abs radios" style="top:642px"><span><i class="radio on"></i>containing</span><span><i class="radio"></i>not containing</span></div>
  <div class="abs keyword"></div>
  <div class="abs search-btn" style="left:173px;top:654px;width:14px;height:16px">
    <svg width="14" height="16" viewBox="0 0 14 16"><circle cx="6.5" cy="7" r="3" fill="none" stroke="#fff" stroke-width="1.4"/><line x1="8.5" y1="9" x2="11" y2="11.5" stroke="#fff" stroke-width="1.6"/></svg>
  </div>

  <div class="abs label-green" style="top:676px">daily deal partners:</div>
  <div class="abs select" style="top:697px;display:flex;align-items:center"><span class="check" style="border:1px solid #888">✓</span>show all<span class="drop-arrow"></span></div>
</aside>

<nav class="abs tabs">
  <div class="tab">LIST VIEW</div>
  <div class="tab">MAP VIEW</div>
  <div class="tab">PREVIOUS DEALS</div>
</nav>
<div class="abs social" style="left:869px;top:62px"><span class="sq s1"></span><span class="sq s2"></span><span class="sq s3"></span><span class="sq s4"></span></div>

<div class="abs sheet"></div>

<article class="deal" style="top:100px">
  <div class="photo" role="img" aria-label="City skyline at night with light trails and a clock tower" style="background:linear-gradient(135deg,#1b1f5a,#6a3aa8 45%,#d84a7a 60%,#2a2f6a)"></div>
  <div class="share"><span class="sq s1"></span><span class="sq s2"></span><span class="sq s3"></span><span class="sq s4"></span><span class="share-pill">share with a friend</span></div>
  <div class="info">
    <div class="title">London / <em>Education &amp; Training</em></div>
    <div class="desc">London Night Photography Class From Piccadilly Circus for £29 (60% Off)</div>
    <div class="meta">From: Tallymob</div>
    <div class="meta">Picked at: 20/11/2011</div>
    <div class="price">29,00</div>
  </div>
  <div class="stats"><div><span>Worth</span><span>73.00</span></div><div><span>Discount</span><span>60%</span></div><div><span>Saving</span><span>44.00</span></div><div><span>Deals sold</span><span>1085</span></div></div>
  <div class="cta details">DETAILS</div><div class="cta buy">BUY NOW !</div>
  <div class="cut"></div>
  <svg class="scissors" width="12" height="12" viewBox="0 0 12 12"><circle cx="3" cy="9" r="2" fill="none" stroke="#888"/><circle cx="9" cy="9" r="2" fill="none" stroke="#888"/><path d="M4 8 10 1M8 8 2 1" stroke="#888"/></svg>
</article>

<article class="deal" style="top:257px">
  <div class="photo" role="img" aria-label="Spa facial massage scene" style="background:linear-gradient(135deg,#f4ece6,#e8cdbb 55%,#c9a58a)"></div>
  <div class="share"><span class="sq s1"></span><span class="sq s2"></span><span class="sq s3"></span><span class="sq s4"></span><span class="share-pill">share with a friend</span></div>
  <div class="info">
    <div class="title">London / <em>Beauty</em></div>
    <div class="desc">Hour Long Massage and Dermavelle Facial for £32 at Lumen Rooms (64% Off)</div>
    <div class="meta">From: Tallymob</div>
    <div class="meta">Picked at: 20/11/2011</div>
    <div class="price">32,00</div>
  </div>
  <div class="stats"><div><span>Worth</span><span>73.00</span></div><div><span>Discount</span><span>60%</span></div><div><span>Saving</span><span>44.00</span></div><div><span>Deals sold</span><span>1085</span></div></div>
  <div class="cta details">DETAILS</div><div class="cta buy">BUY NOW !</div>
  <div class="cut"></div>
  <svg class="scissors" width="12" height="12" viewBox="0 0 12 12"><circle cx="3" cy="9" r="2" fill="none" stroke="#888"/><circle cx="9" cy="9" r="2" fill="none" stroke="#888"/><path d="M4 8 10 1M8 8 2 1" stroke="#888"/></svg>
</article>

<article class="deal" style="top:414px">
  <div class="photo" role="img" aria-label="Plated steak with chips and vegetables" style="background:linear-gradient(160deg,#efe6d6,#c99a52 45%,#5a3018 75%,#2f4a20)"></div>
  <div class="share"><span class="sq s1"></span><span class="sq s2"></span><span class="sq s3"></span><span class="sq s4"></span><span class="share-pill">share with a friend</span></div>
  <div class="info">
    <div class="title">London / <em>Dining</em></div>
    <div class="desc">Two Course Anglo-French Meal For Two With Glass of Wine Each for £20 at Harlow and Pike (Up to 62% Off)</div>
    <div class="meta">From: Tallymob</div>
    <div class="meta">Picked at: 20/11/2011</div>
    <div class="price">20,00</div>
  </div>
  <div class="stats"><div><span>Worth</span><span>73.00</span></div><div><span>Discount</span><span>60%</span></div><div><span>Saving</span><span>44.00</span></div><div><span>Deals sold</span><span>1085</span></div></div>
  <div class="cta details">DETAILS</div><div class="cta buy">BUY NOW !</div>
  <div class="cut"></div>
  <svg class="scissors" width="12" height="12" viewBox="0 0 12 12"><circle cx="3" cy="9" r="2" fill="none" stroke="#888"/><circle cx="9" cy="9" r="2" fill="none" stroke="#888"/><path d="M4 8 10 1M8 8 2 1" stroke="#888"/></svg>
</article>

<article class="deal" style="top:571px">
  <div class="photo" role="img" aria-label="Garden centre with a stone statue and pink flowers" style="background:linear-gradient(160deg,#2e3a22,#6b6a4a 40%,#c8559a 70%,#3f6a2a)"></div>
  <div class="share"><span class="sq s1"></span><span class="sq s2"></span><span class="sq s3"></span><span class="sq s4"></span><span class="share-pill">share with a friend</span></div>
  <div class="info">
    <div class="title">London / <em>Services</em></div>
    <div class="desc">£15 for a £30 Voucher Towards Plants, Christmas Trees and Garden Products at The Fernhill Garden Centre (50% Off)</div>
    <div class="meta">From: Tallymob</div>
    <div class="meta">Picked at: 20/11/2011</div>
    <div class="price">20,00</div>
  </div>
  <div class="stats"><div><span>Worth</span><span>73.00</span></div><div><span>Discount</span><span>60%</span></div><div><span>Saving</span><span>44.00</span></div><div><span>Deals sold</span><span>1085</span></div></div>
  <div class="cta details">DETAILS</div><div class="cta buy">BUY NOW !</div>
  <div class="cut"></div>
  <svg class="scissors" width="12" height="12" viewBox="0 0 12 12"><circle cx="3" cy="9" r="2" fill="none" stroke="#888"/><circle cx="9" cy="9" r="2" fill="none" stroke="#888"/><path d="M4 8 10 1M8 8 2 1" stroke="#888"/></svg>
</article>

<article class="deal" style="top:728px">
  <div class="photo" role="img" aria-label="Gym interior with people on treadmills" style="background:linear-gradient(135deg,#eef2f4,#b8c4cc 50%,#3a3f46)"></div>
  <div class="share"><span class="sq s1"></span><span class="sq s2"></span><span class="sq s3"></span><span class="sq s4"></span><span class="share-pill">share with a friend</span></div>
  <div class="info">
    <div class="title">London / <em>Health &amp; Wellness</em></div>
    <div class="desc">£15 for a £30 Voucher Towards Plants, Christmas Trees and Garden Products at The Fernhill Garden Centre (50% Off)</div>
    <div class="meta">From: Tallymob</div>
    <div class="meta">Picked at: 20/11/2011</div>
    <div class="price">20,00</div>
  </div>
  <div class="stats"><div><span>Worth</span><span>73.00</span></div><div><span>Discount</span><span>60%</span></div><div><span>Saving</span><span>44.00</span></div><div><span>Deals sold</span><span>1085</span></div></div>
  <div class="cta details">DETAILS</div><div class="cta buy">BUY NOW !</div>
</article>
</body>
</html>
```